依頼概要
■依頼の目的/概要
5月~販売する居酒屋のPOPのデザインをお願いします。

■依頼詳細
メニューブック・又は看板に告知用として貼り付けます。

■重視する点
ジンギスカンは臭いイメージがあるので、そこを覆す
『他店とは違う商品』『専門業者』がわかるようなPOPを
Illustrator・Photoshopの経験必須でお願いします。
お客様の目線に立ったデザインをしていただきたいのです。

その他何かご不明な点がございましたら、お気軽にご質問下さい。
よろしくお願いいたします。
店舗の ロゴを追加します。

店名『松葉亭 別館』
松葉亭別館 ロゴデータ追加
出来てますか??
■ 選んだ理由

スッキリと告知!をメインに打ち出していただき、共感できました。

■ 提案者全員のお礼・コメント

定期的に制作があるので、お願いしたいです。

```html
<!DOCTYPE html>
<html lang="ja">
<head>
<meta charset="utf-8">
<title>松葉亭 別館 ジンギスカン 夏季限定</title>
<link rel="stylesheet" href="https://fonts.googleapis.com/css2?family=Dela+Gothic+One&family=Noto+Serif+JP:wght@700;900&family=Noto+Sans+JP:wght@700;900&display=swap">
<style>
:root{
  --ink:#120c08;
  --night:#1d140e;
  --grill-hi:#b8875a;
  --grill-mid:#6e4428;
  --grill-low:#2a1a10;
  --gold-hi:#fff3a8;
  --gold:#f2c94c;
  --gold-deep:#c98a12;
  --red:#c8141b;
  --red-deep:#8e0a10;
  --white:#ffffff;
  --cream:#f7ecd6;
}
*{margin:0;padding:0;box-sizing:border-box}
html,body{width:849px;height:1200px;overflow:hidden;background:var(--ink)}
.poster{position:relative;width:849px;height:1200px;overflow:hidden;background:var(--ink);font-family:"Noto Sans JP",sans-serif}
.grill-photo{position:absolute;left:0;top:90px;width:849px;height:860px;
  background:
    radial-gradient(ellipse 55% 45% at 38% 48%, var(--grill-hi) 0%, var(--grill-mid) 45%, transparent 80%),
    radial-gradient(ellipse 40% 30% at 85% 30%, #5f7a3a 0%, transparent 70%),
    linear-gradient(180deg, var(--grill-low) 0%, var(--grill-mid) 40%, var(--grill-low) 100%);}
.bottom-shade{position:absolute;left:0;top:620px;width:849px;height:580px;
  background:linear-gradient(180deg, transparent 0%, rgba(18,12,8,.85) 28%, var(--ink) 55%, var(--night) 88%, var(--gold-deep) 100%)}
.top-shade{position:absolute;left:0;top:0;width:849px;height:200px;background:linear-gradient(180deg,var(--ink) 45%,transparent)}
.shop-name{position:absolute;left:50px;top:48px;display:flex;align-items:center;gap:12px;
  font-family:"Noto Serif JP",serif;font-weight:900;font-size:44px;color:var(--white);letter-spacing:.04em}
.shop-name .mark{width:30px;height:30px;border-radius:50%;background:var(--red)}
.vertical{position:absolute;writing-mode:vertical-rl;white-space:nowrap}
.tagline{left:722px;top:50px;font-family:"Noto Serif JP",serif;font-weight:900;font-size:40px;color:var(--cream);letter-spacing:.06em;text-shadow:0 2px 6px rgba(0,0,0,.7)}
.title{left:568px;top:105px;font-family:"Dela Gothic One",sans-serif;font-size:120px;line-height:1;letter-spacing:-.02em;
  color:var(--gold);-webkit-text-stroke:5px var(--red-deep);paint-order:stroke fill;
  text-shadow:4px 6px 10px rgba(0,0,0,.6)}
.season{left:708px;top:560px;font-family:"Noto Serif JP",serif;font-weight:900;font-size:30px;color:var(--white);letter-spacing:.06em;text-shadow:0 2px 4px #000}
.reserve{left:766px;top:640px;font-family:"Noto Serif JP",serif;font-weight:900;font-size:46px;color:var(--red);letter-spacing:.02em;
  -webkit-text-stroke:6px var(--white);paint-order:stroke fill}
.summer-badge{position:absolute;left:580px;top:855px;width:146px;height:146px;background:var(--red);border:4px solid var(--gold);
  display:grid;grid-template-columns:1fr 1fr;grid-template-rows:1fr 1fr;writing-mode:vertical-rl;
  font-family:"Noto Serif JP",serif;font-weight:900;font-size:54px;color:var(--white);line-height:1}
.summer-badge span{display:flex;align-items:center;justify-content:center}
.catch{left:312px;top:250px;font-family:"Noto Serif JP",serif;font-weight:900;font-size:36px;color:var(--white);letter-spacing:.06em;text-shadow:0 2px 6px rgba(0,0,0,.8)}
.season-band{left:256px;top:320px;width:46px;padding:14px 0;background:var(--red-deep);
  font-family:"Noto Serif JP",serif;font-weight:700;font-size:22px;color:var(--white);line-height:46px;text-align:center}
.season-band small{font-size:16px;margin-left:4px}
.offer{position:absolute;left:60px;top:740px;color:var(--white)}
.offer-plan{font-weight:900;font-size:30px;letter-spacing:.02em}
.offer-price{margin-top:2px;font-family:"Noto Serif JP",serif;font-weight:900;font-size:122px;line-height:1.05;
  color:var(--red);-webkit-text-stroke:6px var(--gold);paint-order:stroke fill;letter-spacing:-.02em}
.offer-price .yen{font-size:64px}
.offer-price .tax{font-family:"Noto Sans JP",sans-serif;font-size:22px;color:var(--white);-webkit-text-stroke:0;vertical-align:8px;margin-left:4px}
.offer-extra{margin-top:6px;font-weight:700;font-size:24px;color:var(--gold)}
.offer-extra b{color:var(--red);font-size:30px;-webkit-text-stroke:4px var(--white);paint-order:stroke fill}
</style>
</head>
<body>
<main class="poster">
  <div class="grill-photo" role="img" aria-label="鉄鍋で焼けるジンギスカンの羊肉と野菜、箸で持ち上げた肉の写真"></div>
  <div class="top-shade"></div>
  <div class="bottom-shade"></div>

  <div class="shop-name"><span class="mark"></span>松葉亭 別館</div>

  <p class="vertical tagline">奇跡のおいしさ</p>
  <h1 class="vertical title">ジンギスカン</h1>
  <p class="vertical season">五月から八月</p>
  <p class="vertical reserve">先行予約受付中</p>
  <div class="summer-badge"><span>夏</span><span>季</span><span>限</span><span>定</span></div>

  <p class="vertical catch">これぞ、ジンギスカン！</p>
  <p class="vertical season-band"><small>松葉亭別館</small> 夏の定番、スタート</p>

  <section class="offer">
    <p class="offer-plan">3時間飲み放題つき/全6品</p>
    <p class="offer-price">3,680<span class="yen">円</span><span class="tax">税別</span></p>
    <p class="offer-extra"><b>+500</b>円(税別)で食べ放題</p>
  </section>
</main>
</body>
</html>
```